DOUBLE SIDED BROCHURE NEEDED TO PROMOTE DOCTOR

I need a double sided DL size (99mm x 210mm) brochure, promoting a doctor seeing patients in a new area.

I want something professional. I have included the relevant information. I would also like the Dr's picture somwhere in the brochure, with a professional background. I wish to print these tomorrow, so i will pick a winner within 14 hours of posting this ad.

I have included an example of a brochures design that I recently saw, and its definietly a good starting point.

Industry/Entity Type

Medical

```html
<!DOCTYPE html>
<html lang="en">
<head>
<meta charset="utf-8">
<title>Surgeon Referral Brochure – DL Double Sided</title>
<link rel="stylesheet" href="https://fonts.googleapis.com/css2?family=Montserrat:wght@600;700&family=Open+Sans:wght@400;600;700&display=swap">
<style>
  :root {
    --blue: #1c9edb;
    --blue-light: #8fc7ea;
    --green: #76bc43;
    --panel: #efefef;
    --curve-grey: #c9c9c9;
    --ink: #2b2b2b;
    --stage: #e4e7ea;
  }
  * { box-sizing: border-box; margin: 0; padding: 0; }
  html, body { width: 1098px; height: 1200px; overflow: hidden; }
  body {
    background: var(--stage);
    font-family: "Open Sans", Arial, sans-serif;
    color: var(--ink);
    position: relative;
  }
  .brochure-side {
    position: absolute;
    top: 70px;
    width: 500px;
    height: 1060px;
    background: var(--panel);
    overflow: hidden;
    box-shadow: 0 6px 18px rgba(0,0,0,0.18);
  }
  .side-front { left: 33px; }
  .side-back { left: 565px; }

  /* Front */
  .team-photo {
    position: absolute; left: 0; top: 0; width: 500px; height: 380px;
    background: linear-gradient(180deg, var(--blue) 0%, #3aaee3 55%, #e9eef2 100%);
  }
  .header-curve { position: absolute; left: 0; top: 300px; width: 500px; height: 110px; }
  .greeting {
    position: absolute; left: 0; top: 390px; width: 500px; text-align: center;
    font-family: "Montserrat", Arial, sans-serif; font-weight: 600;
    font-size: 30px; color: var(--blue);
  }
  .announcement {
    position: absolute; left: 50px; width: 400px; text-align: center;
    font-size: 20px; line-height: 1.5;
  }
  .announcement-intro { top: 445px; }
  .announcement-terms { top: 590px; }
  .clinic-pin { position: absolute; left: 236px; top: 790px; width: 28px; height: 38px; }
  .clinic-name {
    position: absolute; left: 0; top: 832px; width: 500px; text-align: center;
    font-family: "Montserrat", Arial, sans-serif; font-weight: 700;
    font-size: 32px; color: var(--blue); letter-spacing: 1px;
  }
  .clinic-address {
    position: absolute; left: 0; top: 876px; width: 500px; text-align: center; font-size: 19px;
  }
  .phone-band {
    position: absolute; left: 0; top: 920px; width: 500px; height: 66px;
    background: var(--green); color: #fff; text-align: center; line-height: 66px;
    font-family: "Montserrat", Arial, sans-serif; font-weight: 700; font-size: 32px;
  }
  .fax-label {
    position: absolute; left: 0; top: 1002px; width: 500px; text-align: center;
    font-size: 18px; font-weight: 600;
  }
  .fax-number {
    position: absolute; left: 0; top: 1020px; width: 500px; text-align: center;
    font-family: "Montserrat", Arial, sans-serif; font-weight: 700; font-size: 34px; color: var(--green);
  }

  /* Back */
  .top-band { position: absolute; left: 0; top: 0; width: 500px; height: 170px; }
  .portrait-frame {
    position: absolute; left: 80px; top: 0; width: 340px; height: 300px;
    border: 6px solid var(--blue-light); border-top: none;
    border-radius: 0 0 170px 170px; overflow: hidden; background: #fff;
  }
  .portrait-photo {
    width: 100%; height: 100%;
    background: linear-gradient(160deg, #b9d6ee 0%, #8bb3d6 45%, #5d6f80 75%, #2f3a45 100%);
  }
  .surgeon-name {
    position: absolute; left: 0; top: 328px; width: 500px; text-align: center;
    font-family: "Montserrat", Arial, sans-serif; font-weight: 600; font-size: 28px; color: var(--blue);
  }
  .surgeon-intro {
    position: absolute; left: 40px; top: 372px; width: 420px; text-align: center;
    font-size: 19px; line-height: 1.5;
  }
  .procedure-list { position: absolute; left: 40px; width: 440px; list-style: none; }
  .procedure-list li {
    position: relative; padding-left: 30px; font-size: 19px; line-height: 1.25; margin-bottom: 20px;
  }
  .procedure-list li::before {
    content: ""; position: absolute; left: 0; top: 9px; width: 10px; height: 10px;
    border-radius: 50%; background: var(--blue);
  }
  .procedure-list small { display: block; font-size: 15px; }
  .list-specialist { top: 540px; }
  .list-general { top: 760px; }
  .general-band {
    position: absolute; left: 40px; top: 690px; width: 420px; height: 44px;
    background: var(--green); color: #fff; line-height: 44px; padding-left: 22px;
    font-weight: 700; font-size: 19px;
  }
  .bottom-stripe {
    position: absolute; left: 0; bottom: 0; width: 500px; height: 34px;
    background: var(--blue); border-top: 4px solid #1a1a1a;
  }
</style>
</head>
<body>

<section class="brochure-side side-front">
  <div class="team-photo" role="img" aria-label="Group photo of five smiling doctors in white coats against a blue background"></div>
  <svg class="header-curve" viewBox="0 0 500 110" preserveAspectRatio="none" aria-hidden="true">
    <path d="M0 80 Q250 10 500 40 L500 110 L0 110 Z" fill="var(--curve-grey)"/>
    <path d="M0 92 Q250 22 500 52 L500 110 L0 110 Z" fill="var(--panel)"/>
  </svg>

  <h2 class="greeting">Dear Doctors,</h2>
  <p class="announcement announcement-intro">We are pleased to announce that Dr. Samir Nadeem is now consulting in Mandurah, seeing public and private patients.</p>
  <p class="announcement announcement-terms">Guaranteed appointment within two weeks, with patients having the option of surgery at Coastal Health Campus, Southgate Hospital or St. Luke's Riverside.</p>

  <svg class="clinic-pin" viewBox="0 0 28 38" aria-hidden="true">
    <path d="M14 2 C7 2 3 7 3 13 C3 21 14 30 14 30 C14 30 25 21 25 13 C25 7 21 2 14 2 Z" fill="#e85a6b"/>
    <circle cx="14" cy="13" r="4.5" fill="#fff"/>
    <ellipse cx="14" cy="34" rx="8" ry="2.5" fill="none" stroke="#999" stroke-width="1.5"/>
  </svg>
  <h3 class="clinic-name">MANDURAH CLINIC:</h3>
  <p class="clinic-address">48 Harbourside Drive Mandurah WA 6210</p>
  <div class="phone-band">Phone: 1300 482 716</div>
  <p class="fax-label">Please send all referrals by fax to</p>
  <p class="fax-number">(08) 6100 2485</p>
</section>

<section class="brochure-side side-back">
  <svg class="top-band" viewBox="0 0 500 170" preserveAspectRatio="none" aria-hidden="true">
    <path d="M0 0 H500 V120 Q250 100 0 145 Z" fill="var(--blue)"/>
    <path d="M0 145 Q250 100 500 120 V132 Q250 112 0 157 Z" fill="var(--curve-grey)"/>
  </svg>
  <div class="portrait-frame">
    <div class="portrait-photo" role="img" aria-label="Portrait of the surgeon in a dark blazer in front of a modern hospital building under a blue sky"></div>
  </div>

  <h2 class="surgeon-name">Dr. Nadeem</h2>
  <p class="surgeon-intro">is a highly trained specialised surgeon, in all areas of Endocrine, Breast and General Surgery. Including;</p>

  <ul class="procedure-list list-specialist">
    <li>Thyroid Surgery</li>
    <li>Parathyroid surgery<small>(including minimally invasive parathyroidectomy)</small></li>
    <li>Breast Cancer<small>(Benign breast lesions)</small></li>
  </ul>

  <div class="general-band">All areas of general surgery, such as;</div>

  <ul class="procedure-list list-general">
    <li>Gallbladder surgery</li>
    <li>Hernia surgery</li>
    <li>Haemorrhoids</li>
    <li>Carpal Tunnel</li>
    <li>Vasectomy etcetc...</li>
  </ul>

  <div class="bottom-stripe"></div>
</section>

</body>
</html>
```